Website for peer to peer car sharing service

Hi all,

We need a web design for a new environmental friendly peer-to-peer car sharing website.

The website will serve as a marketplace where car owners can list their car and drivers that who do not have access to a car can rent a suitable car. It is important for us to emphasis that this is a community where the main purpose is to use the vehicles on the street in a more efficient way.

Attached are five pictures where we have sketched up the five main pages:

File 1. Info site for a particular car.
File 2. Logo.
File 3. Register a car.
File 4. Sign up.
File 5. Search.
File 6. Front page.

The logo for the company is attached (File 2) and it would be ideal to design the website in relation to the logo. The final design should relate to a secure market place which is environmental friendly.

We would like this webpage to be in the same spirit as www.velnoro.it, www.brundale.com, www.plimtrovesite.com, https://wend.kul.net, https://garbelow.com etc.

We look forward to see your designs.

Best regards,
The Trundo Team.

Hi guys, 

Please take :

1) Could you please design icons for for  'FAQ' and 'Insurance' in the header, locate the icons right to the Trundo logo. We only want two icons ('FAQ' and 'Insurance')  right to the Trundo logo.

2) The height of the header should be the same as the header of faplex.com

3) The price tags for the cars (below the top section) should be similar to the price tags at mostanbee.com.

4) We would like you to start to design the other pages (the sub-pages listed in the project description:
a)Info site for a particular car.
b)Register a car. 
c)Search results (similar to http://www.pevrotank.com/find-car).

Please take a look at the picture attached for the sub-pages:

https://files.quenmolt.example/brief_uploads/000001_3_search_000001_brief000001.jpg

https://files.quenmolt.example/brief_uploads/000002_4_infositeforaparticularcar_000002_brief000002.jpg

http://www.quenmolt.example/file.aspx?fileLocation=storage_url/brief_uploads/000003_5_registeracar_brief000003.jpg

Best regards, 
Trundo team 

Target Market(s)

The target market are people from 20-40 years old who are environmental friendly, also tourists who visit the city and would like to rent a car.

Industry/Entity Type

It Company

Requirements
Must have
• It is required that the designer that will be chosen will hand in layered PSD files of each web page.

```html
<!DOCTYPE html>
<html lang="en">
<head>
<meta charset="utf-8">
<title>Trundo – Car Details</title>
<link rel="stylesheet" href="https://fonts.googleapis.com/css2?family=Kreon:wght@300;400;700&display=swap">
<style>
:root{
  --green:#6fbf1d;
  --green-dark:#4f9a0c;
  --green-light:#9ad94a;
  --text:#333333;
  --text-soft:#555555;
  --muted:#8a8a8a;
  --line:#d9d9d9;
  --panel:#f6f6f6;
  --header-top:#4d4d4d;
  --header-bottom:#7b7b7b;
  --footer:#3b3b3b;
  --footer-text:#a9a9a9;
  --red:#e3211f;
  --white:#ffffff;
}
*{box-sizing:border-box;margin:0;padding:0}
html,body{width:1200px;height:2345px;overflow:hidden}
body{position:relative;background:var(--white);color:var(--text);font-family:"Kreon",Georgia,serif;font-size:15px}
.abs{position:absolute}

/* Header */
.site-header{left:0;top:0;width:1200px;height:102px;background:linear-gradient(var(--header-top),var(--header-bottom));}
.brand{left:150px;top:20px;display:flex;align-items:center;gap:14px;color:var(--white);font-weight:700;font-size:44px;line-height:1}
.brand-dot{width:42px;height:42px;border-radius:50%;background:var(--green)}
.main-nav{left:752px;top:22px;display:flex;gap:18px;color:var(--white);font-size:15px}
.welcome{left:916px;top:12px;width:150px;height:36px;background:var(--white);border-radius:4px;font-size:14px;color:#222;display:flex;align-items:center;justify-content:center}
.social{display:flex;gap:10px}
.social span{width:28px;height:28px;border-radius:50%;background:#f2f2f2;display:block}
.header-social{left:924px;top:62px}

/* Hero */
.hero{left:0;top:102px;width:1200px;height:513px;background:radial-gradient(ellipse at 75% 45%,#7a7f86 0%,#5a6068 45%,#3d4148 100%)}
.hero-photo{left:0;top:0;width:1200px;height:513px;background:linear-gradient(90deg,rgba(40,44,50,.55),rgba(110,115,122,.15) 55%,rgba(60,64,70,.35))}
.hero-tag{left:131px;top:101px;width:461px;height:43px;background:rgba(60,60,60,.82);color:var(--white);font-size:25px;padding:6px 16px;letter-spacing:.5px}
.hero-title{left:147px;top:177px;width:390px;color:var(--white);font-size:25px;line-height:28px;letter-spacing:.4px;font-weight:400}
.hero-text{left:147px;top:261px;width:370px;color:var(--white);font-size:13.5px;line-height:24.5px}
.hero-car{left:625px;top:92px;width:490px;height:285px;border-radius:120px 140px 60px 60px;background:linear-gradient(#d9d7d2,#a9a7a2)}
.hero-arrow{top:187px;width:49px;height:53px;background:rgba(30,30,30,.75);display:flex;align-items:center;justify-content:center}
.hero-arrow.prev{left:39px}.hero-arrow.next{left:1118px}
.hero-dots{left:575px;top:461px;display:flex;gap:7px}
.hero-dots span{width:11px;height:11px;border-radius:50%;background:#e6e6e6}
.hero-dots span.on{background:var(--green)}

/* Features */
.features{left:0;top:615px;width:1200px;height:157px;background:linear-gradient(#ffffff,#efefea)}
.feature{top:22px;width:300px;height:110px}
.feature-icon{left:0;top:0;width:92px;height:92px}
.feature h3{position:absolute;left:108px;top:12px;font-weight:300;font-size:35px;color:#5a5a5a;line-height:1}
.feature p{position:absolute;left:110px;top:56px;width:170px;font-size:13px;line-height:15px;color:var(--muted)}

/* Section headings */
.section-title{font-size:22px;font-weight:400;letter-spacing:.6px;color:#222}

/* Gallery */
.gallery-tabs{left:139px;top:875px;width:108px}
.gallery-tabs li{list-style:none;height:38px;margin-bottom:4px;background:#d8d8d8;font-size:15px;padding:8px 0 0 12px;color:#333}
.gallery-tabs li.active{background:var(--green);color:var(--white);display:flex;align-items:center;gap:8px;padding:0 0 0 6px}
.tab-icon{width:24px;height:18px;background:var(--white);border-radius:2px}
.gallery-main{left:248px;top:862px;width:409px;height:267px;border:5px solid var(--green);background:linear-gradient(160deg,#3b2e27,#7d3a2a 40%,#b8412d 60%,#4a4440)}
.thumb{top:1139px;width:112px;height:84px;border:4px solid var(--green);background:linear-gradient(160deg,#3b2e27,#b8412d 55%,#4a4440)}

.description{left:139px;top:1305px;width:518px;font-size:14.5px;line-height:24.5px;color:var(--text)}

/* Reviews */
.trip-name{left:139px;top:1482px;color:var(--green);font-size:22px;letter-spacing:.4px}
.overall{left:139px;top:1516px;font-size:15px}
.overall em{font-style:normal;color:var(--green)}
.rating-count{left:558px;top:1516px;font-size:15px}
.reviews{left:139px;top:1557px;width:518px}
.review{border-top:2px solid var(--line);padding:14px 0 0}
.review:first-child{height:196px}.review:nth-child(2){height:152px}.review:nth-child(3){height:146px}
.review-avatar{float:left;width:63px;height:61px;border:1px solid var(--line);margin:0 21px 4px 13px;display:flex;align-items:center;justify-content:center}
.review-head{display:flex;align-items:center;height:22px;font-size:14.5px}
.review-date{margin-left:20px;font-size:11.5px}
.stars{margin-left:auto;display:flex;gap:2px}
.review p{font-size:12.5px;line-height:23.5px;color:var(--text-soft)}

/* Booking */
.booking{left:717px;top:862px;width:348px;height:486px;background:var(--panel);border:1px solid #e2e2e2;border-radius:5px}
.option{left:24px;display:flex;align-items:center;gap:16px;font-size:18px;color:#222}
.option i{width:12px;height:12px;border:1px solid #aaa;background:var(--white);display:block}
.rule{left:10px;width:328px;height:1px;background:#d8d8d8}
.field-label{font-size:18px;color:#222}
.select{height:34px;background:var(--white);border:1px solid #cfcfcf;border-radius:3px;font-size:12px;padding:9px 8px;color:#444}
.select::after{content:"";position:absolute;right:9px;top:14px;border:6px solid transparent;border-top-color:#777;border-bottom:0}
.subtotal{left:18px;top:372px;font-size:22px;color:#222}
.subtotal b{font-weight:400;color:var(--red);margin-left:10px}
.book-btn{left:17px;top:406px;width:319px;height:50px;border-radius:5px;background:linear-gradient(var(--green-light),var(--green-dark));color:var(--white);font-size:26px;display:flex;align-items:center;justify-content:center;letter-spacing:.5px}

/* Owner */
.owner{left:717px;top:1426px;width:348px;height:356px;background:var(--panel);border:1px solid #e2e2e2;border-radius:5px}
.owner-avatar{left:18px;top:10px;width:106px;height:108px;background:linear-gradient(#eaf0f6,#c9d5e2)}
.owner-name{left:141px;top:18px;font-size:19px;color:#555}
.owner-text{left:141px;top:46px;width:195px;font-size:13px;line-height:19px;color:var(--text-soft)}
.owner-map{left:16px;top:142px;width:320px;height:196px;border-radius:4px;background:linear-gradient(135deg,#dfe7c9,#efe9d8 45%,#a9c7e2 70%,#8fb6d9)}

.promo{left:717px;top:1821px;width:348px;height:197px;border-radius:5px;background:linear-gradient(90deg,#2d3a4b,#56637a 45%,#c49a7a 75%,#6f5a4e)}
.promo-text{left:18px;top:10px;color:var(--white);font-size:35px;line-height:43px;font-weight:700}

/* Footer */
.site-footer{left:0;top:2083px;width:1200px;height:262px;background:var(--footer);color:var(--footer-text)}
.footer-col{top:24px}
.footer-head{display:flex;align-items:center;gap:14px;color:var(--white);font-size:17px;font-style:italic;font-weight:700;letter-spacing:.4px}
.footer-text{font-size:12.5px;line-height:24px}
.gateways li{list-style:none;font-size:12.5px;line-height:24.5px}
.footer-brand{left:854px;top:184px;display:flex;align-items:center;gap:12px;color:#8c8c8c;font-weight:700;font-size:42px}
.footer-brand .brand-dot{background:#6a6a6a;width:38px;height:38px}
</style>
</head>
<body>

<header class="site-header abs">
  <div class="brand abs"><span class="brand-dot"></span>Trundo</div>
  <nav class="main-nav abs"><span>Home</span><span>About</span><span>Contact</span></nav>
  <div class="welcome abs">Welcome Username !</div>
  <div class="social header-social abs"><span></span><span></span><span></span><span></span></div>
</header>

<section class="hero abs">
  <div class="hero-photo abs" role="img" aria-label="Blurred photo of a woman driving a car"></div>
  <div class="hero-car abs" role="img" aria-label="Silver compact SUV"></div>
  <div class="hero-tag abs">SEARCH FOR 'LOREM IPSUM' WILL</div>
  <h1 class="hero-title abs">UNCOVER MANY WEB SITES STILL IN THEIR INFANCY.</h1>
  <p class="hero-text abs">Many desktop publishing packages and web page editors now use Lorem Ipsum as their default model text, and a search for 'lorem ipsum' will uncover many web sites still in their infancy. Various versions have evolved over the years</p>
  <div class="hero-arrow prev abs"><svg width="14" height="20" viewBox="0 0 14 20"><path d="M11 2 3 10l8 8" fill="none" stroke="#fff" stroke-width="3"/></svg></div>
  <div class="hero-arrow next abs"><svg width="14" height="20" viewBox="0 0 14 20"><path d="M3 2l8 8-8 8" fill="none" stroke="#fff" stroke-width="3"/></svg></div>
  <div class="hero-dots abs"><span class="on"></span><span></span><span></span></div>
</section>

<section class="features abs">
  <div class="feature abs" style="left:129px">
    <svg class="feature-icon abs" viewBox="0 0 92 92"><rect x="16" y="16" width="60" height="60" rx="10" transform="rotate(45 46 46)" fill="#fff" stroke="#222" stroke-width="5"/><path d="M26 48l14 14 34-36" fill="none" stroke="#6fbf1d" stroke-width="10" stroke-linecap="round" stroke-linejoin="round"/></svg>
    <h3>Quality</h3><p>standard dummy text ever since the 1500s, when an unknown printer</p>
  </div>
  <div class="feature abs" style="left:448px">
    <svg class="feature-icon abs" viewBox="0 0 92 92"><rect x="16" y="16" width="60" height="60" rx="10" transform="rotate(45 46 46)" fill="#fff" stroke="#222" stroke-width="5"/><path d="M26 48l14 14 34-36" fill="none" stroke="#6fbf1d" stroke-width="10" stroke-linecap="round" stroke-linejoin="round"/></svg>
    <h3>Reliability</h3><p>standard dummy text ever since the 1500s, when an unknown printer</p>
  </div>
  <div class="feature abs" style="left:773px">
    <svg class="feature-icon abs" viewBox="0 0 92 92"><rect x="16" y="16" width="60" height="60" rx="10" transform="rotate(45 46 46)" fill="#fff" stroke="#222" stroke-width="5"/><path d="M26 48l14 14 34-36" fill="none" stroke="#6fbf1d" stroke-width="10" stroke-linecap="round" stroke-linejoin="round"/></svg>
    <h3>Convenience</h3><p>standard dummy text ever since the 1500s, when an unknown printer</p>
  </div>
</section>

<h2 class="section-title abs" style="left:139px;top:810px">CAR NAME</h2>
<ul class="gallery-tabs abs">
  <li class="active"><span class="tab-icon"></span>Pictures</li>
  <li>Map</li>
  <li>Calendar</li>
</ul>
<div class="gallery-main abs" role="img" aria-label="Red SUV front view"></div>
<div class="thumb abs" style="left:246px" role="img" aria-label="Red SUV thumbnail"></div>
<div class="thumb abs" style="left:369px" role="img" aria-label="Red SUV thumbnail"></div>
<div class="thumb abs" style="left:492px" role="img" aria-label="Red SUV thumbnail"></div>

<h2 class="section-title abs" style="left:139px;top:1262px">DESCRIPTION</h2>
<p class="description abs">Lorem Ipsum is simply dummy text of the printing and typesetting industry. Lorem Ipsum has been the industry's standard dummy text ever since the 1500s, when an unknown printer took a galley of type and scrambled it to make a type specimen book. It has survived not only five centuries.</p>

<h2 class="section-title abs" style="left:139px;top:1441px">REVIEWS</h2>
<div class="trip-name abs">TRIP NAME LOREM IPSUM</div>
<div class="overall abs">Overall Rating: <em>4/5 Stars</em></div>
<div class="rating-count abs">Rating &nbsp; 150</div>

<div class="reviews abs">
  <article class="review">
    <div class="review-avatar"><svg width="40" height="42" viewBox="0 0 40 42"><circle cx="20" cy="13" r="10" fill="#9a9a9a"/><path d="M2 42c0-12 8-18 18-18s18 6 18 18z" fill="#9a9a9a"/></svg></div>
    <div class="review-head">Username ABCD<span class="review-date">25th Jan, 2013</span>
      <span class="stars">
        <svg width="20" height="19" viewBox="0 0 20 19"><path d="M10 0l3 6.5 7 .7-5.3 4.7 1.6 7L10 15.3 3.7 19l1.6-7L0 7.2l7-.7z" fill="#6fbf1d"/></svg>
        <svg width="20" height="19" viewBox="0 0 20 19"><path d="M10 0l3 6.5 7 .7-5.3 4.7 1.6 7L10 15.3 3.7 19l1.6-7L0 7.2l7-.7z" fill="#6fbf1d"/></svg>
        <svg width="20" height="19" viewBox="0 0 20 19"><path d="M10 0l3 6.5 7 .7-5.3 4.7 1.6 7L10 15.3 3.7 19l1.6-7L0 7.2l7-.7z" fill="#6fbf1d"/></svg>
        <svg width="20" height="19" viewBox="0 0 20 19"><path d="M10 0l3 6.5 7 .7-5.3 4.7 1.6 7L10 15.3 3.7 19l1.6-7L0 7.2l7-.7z" fill="#6fbf1d"/></svg>
        <svg width="20" height="19" viewBox="0 0 20 19"><path d="M10 1l3 6.5 6.5.6-5 4.4 1.5 6.5L10 15.6 4 19l1.5-6.5-5-4.4L7 7.5z" fill="none" stroke="#6fbf1d"/></svg>
      </span></div>
    <p>Lorem Ipsum is simply dummy text of the printing and typesetting industry. Lorem Ipsum has been the industry's standard dummy text ever since the 1500s, when an unknown printer took a galley of type and scrambled it to make a type specimen book. It has survived not only five centuries, but also the leap into electronic typesetting. release of Letraset sheets containing Lorem Ipsum passages release of Letraset sheets containing Lorem Ipsum passages</p>
  </article>
  <article class="review">
    <div class="review-avatar"><svg width="40" height="42" viewBox="0 0 40 42"><circle cx="20" cy="13" r="10" fill="#9a9a9a"/><path d="M2 42c0-12 8-18 18-18s18 6 18 18z" fill="#9a9a9a"/></svg></div>
    <div class="review-head">Username ABCD<span class="review-date">25th Jan, 2013</span>
      <span class="stars">
        <svg width="20" height="19" viewBox="0 0 20 19"><path d="M10 0l3 6.5 7 .7-5.3 4.7 1.6 7L10 15.3 3.7 19l1.6-7L0 7.2l7-.7z" fill="#6fbf1d"/></svg>
        <svg width="20" height="19" viewBox="0 0 20 19"><path d="M10 0l3 6.5 7 .7-5.3 4.7 1.6 7L10 15.3 3.7 19l1.6-7L0 7.2l7-.7z" fill="#6fbf1d"/></svg>
        <svg width="20" height="19" viewBox="0 0 20 19"><path d="M10 0l3 6.5 7 .7-5.3 4.7 1.6 7L10 15.3 3.7 19l1.6-7L0 7.2l7-.7z" fill="#6fbf1d"/></svg>
        <svg width="20" height="19" viewBox="0 0 20 19"><path d="M10 0l3 6.5 7 .7-5.3 4.7 1.6 7L10 15.3 3.7 19l1.6-7L0 7.2l7-.7z" fill="#6fbf1d"/></svg>
        <svg width="20" height="19" viewBox="0 0 20 19"><path d="M10 0l3 6.5 7 .7-5.3 4.7 1.6 7L10 15.3 3.7 19l1.6-7L0 7.2l7-.7z" fill="#6fbf1d"/></svg>
      </span></div>
    <p>Lorem Ipsum is simply dummy text of the printing and typesetting industry. Lorem Ipsum has been the industry's standard dummy text ever since the 1500s, when an unknown printer took a galley of type and scrambled it to make a type specimen book. It has survived not only five centuries.</p>
  </article>
  <article class="review">
    <div class="review-avatar"><svg width="40" height="42" viewBox="0 0 40 42"><circle cx="20" cy="13" r="10" fill="#9a9a9a"/><path d="M2 42c0-12 8-18 18-18s18 6 18 18z" fill="#9a9a9a"/></svg></div>
    <div class="review-head">Username ABCD<span class="review-date">25th Jan, 2013</span>
      <span class="stars">
        <svg width="20" height="19" viewBox="0 0 20 19"><path d="M10 0l3 6.5 7 .7-5.3 4.7 1.6 7L10 15.3 3.7 19l1.6-7L0 7.2l7-.7z" fill="#6fbf1d"/></svg>
        <svg width="20" height="19" viewBox="0 0 20 19"><path d="M10 0l3 6.5 7 .7-5.3 4.7 1.6 7L10 15.3 3.7 19l1.6-7L0 7.2l7-.7z" fill="#6fbf1d"/></svg>
        <svg width="20" height="19" viewBox="0 0 20 19"><path d="M10 0l3 6.5 7 .7-5.3 4.7 1.6 7L10 15.3 3.7 19l1.6-7L0 7.2l7-.7z" fill="#6fbf1d"/></svg>
        <svg width="20" height="19" viewBox="0 0 20 19"><path d="M10 1l3 6.5 6.5.6-5 4.4 1.5 6.5L10 15.6 4 19l1.5-6.5-5-4.4L7 7.5z" fill="none" stroke="#6fbf1d"/></svg>
        <svg width="20" height="19" viewBox="0 0 20 19"><path d="M10 1l3 6.5 6.5.6-5 4.4 1.5 6.5L10 15.6 4 19l1.5-6.5-5-4.4L7 7.5z" fill="none" stroke="#6fbf1d"/></svg>
      </span></div>
    <p>Lorem Ipsum is simply dummy text of the printing and typesetting industry. Lorem Ipsum has been the industry's standard dummy text ever since the 1500s, when an unknown printer took a galley of type and scrambled it to make a type specimen book. It has survived not only five centuries.</p>
  </article>
</div>

<h2 class="section-title abs" style="left:725px;top:810px">BOOKING ONLINE</h2>
<aside class="booking abs">
  <div class="option abs" style="top:20px"><i></i>Price Per Day</div>
  <div class="option abs" style="top:57px"><i></i>Price Per Hour</div>
  <div class="option abs" style="top:94px"><i></i>Price Per Week</div>
  <div class="rule abs" style="top:134px"></div>
  <div class="field-label abs" style="left:18px;top:144px">Start Date</div>
  <div class="field-label abs" style="left:226px;top:144px">Start Time</div>
  <div class="select abs" style="left:19px;top:180px;width:192px"></div>
  <div class="select abs" style="left:222px;top:180px;width:110px">12:00 AM</div>
  <div class="rule abs" style="top:237px"></div>
  <div class="field-label abs" style="left:18px;top:250px">End Date</div>
  <div class="field-label abs" style="left:226px;top:250px">Start Time</div>
  <div class="select abs" style="left:19px;top:286px;width:192px"></div>
  <div class="select abs" style="left:222px;top:286px;width:110px">12:00 AM</div>
  <div class="rule abs" style="top:344px"></div>
  <div class="subtotal abs">SUBTOTAL<b>$200</b></div>
  <div class="book-btn abs">BOOK NOW</div>
</aside>

<h2 class="section-title abs" style="left:725px;top:1374px">OWNER INFO</h2>
<aside class="owner abs">
  <div class="owner-avatar abs" role="img" aria-label="Owner profile picture"></div>
  <div class="owner-name abs">Owner's Name</div>
  <p class="owner-text abs">Owner's description fact that a reader will be distracted by the readable content of a page when looking at its layout.</p>
  <div class="owner-map abs" role="img" aria-label="Street map showing the car's location"></div>
</aside>

<div class="promo abs" role="img" aria-label="Photo of a smiling woman holding car keys">
  <div class="promo-text abs">Get 25%<br>Extra on<br>Each<br>Booking</div>
</div>

<footer class="site-footer abs">
  <div class="footer-col abs" style="left:141px;width:240px">
    <div class="footer-head"><svg width="32" height="22" viewBox="0 0 32 22"><rect width="32" height="22" fill="#fff"/><path d="M0 0l16 12L32 0" fill="none" stroke="#3b3b3b" stroke-width="2.5"/></svg>CONTACT</div>
    <p class="footer-text" style="margin-top:10px">dummy text of the printing, #48307,<br>abcd, AB 317940</p>
    <p style="margin-top:20px;font-size:15px">Support</p>
    <p style="font-size:12.5px;color:var(--green)">hello@trundomail.com</p>
    <div class="social" style="margin-top:30px"><span style="background:#5e5e5e"></span><span style="background:#5e5e5e"></span><span style="background:#5e5e5e"></span><span style="background:#5e5e5e"></span></div>
  </div>
  <div class="footer-col abs" style="left:471px;width:230px">
    <div class="footer-head"><svg width="30" height="30" viewBox="0 0 30 30"><rect x="1" y="4" width="24" height="24" fill="none" stroke="#fff" stroke-width="2.5"/><path d="M10 20l2-6 14-14 4 4-14 14z" fill="#fff"/></svg>TESTIMONIALS</div>
    <p class="footer-text" style="margin-top:8px;font-size:12px;line-height:22px">“ I can't tell you how handy this thing is. How many times do you find your phone running low on battery, and you're without a sync cable on hand for a quick charge? Because PowerSleeve rides in your wallet, it goes where you go.</p>
    <p style="margin-top:22px;font-size:12px">© 2013 Trundo. All rights reserved.</p>
  </div>
  <div class="footer-col abs" style="left:854px;width:240px">
    <div class="footer-head"><svg width="32" height="24" viewBox="0 0 32 24"><path d="M3 11l4-9h18l4 9h2v9h-4v4h-5v-4H10v4H5v-4H1v-9z" fill="#fff"/><circle cx="8" cy="15" r="2.5" fill="#3b3b3b"/><circle cx="24" cy="15" r="2.5" fill="#3b3b3b"/></svg>TOP GATEWAYS</div>
    <ul class="gateways" style="margin-top:6px">
      <li>&gt; &nbsp;Car Rental Cityname Lorem Ipsum</li>
      <li>&gt; &nbsp;Car Rental Cityname Lorem Ipsum</li>
      <li>&gt; &nbsp;Car Rental Cityname Lorem Ipsum</li>
      <li>&gt; &nbsp;Car Rental Cityname Lorem Ipsum</li>
      <li>&gt; &nbsp;Car Rental Cityname Lorem Ipsum</li>
    </ul>
  </div>
  <div class="footer-brand abs"><span class="brand-dot"></span>Trundo</div>
</footer>

</body>
</html>
```